Business Card Design Project (Beer industry)

I am seeking a redesign of my business card. I am looking for something that will really stand out in both texture and feel. Something more on the modern side then traditional. Nothing die cut shaped like a beer mug please.

The card is used mostly for other industry professionals, as well as bar and restaurant owners. My title is Strategy & Acquisitions. If you would like to somehow incorporate that theme, that may work.

My business is craft and imported beer. Nothing fizzy and yellow, so my products are more on the upscale side.
Updates

I was able to update my logo in .ai and .tif format. I hope that helps. 

Thank you all for your creative ideas. I have uploaded my current business card in pdf format, as well as our logo in .eps file format. We are excited about the submissions so far and want to thank you all again.

PS Please do not include fax number in future submissions, as we are looking for something more creative and a fax says 1999 and not 2015, which is the message we are going for, without being futuristic. 

Thank you all once again for all of your submissions. If we would consider a two sided card, we would like the opposite side not to be the same as the front. The styles we have seen so far, it appears the front and back are too similar. Again, a two sided card is not required. Thank you and we look forward to pushing the boundaries of your creativity. Cheers

Target Market(s)

My card would mostly go to bar and restaurant operators as well as other beer industry professionals

Industry/Entity Type

Restaurant

Requirements
Nice to have
• Two sided would be considered, although not required
Should not have
• Anything die cut shaped like a beer mug.

```html
<!DOCTYPE html>
<html lang="en">
<head>
<meta charset="utf-8">
<title>Northvale Beer – Business Card</title>
<link rel="stylesheet" href="https://fonts.googleapis.com/css2?family=Lora:ital,wght@1,400;1,600&family=Questrial&display=swap">
<style>
  :root {
    --stage: #3a3a3a;
    --card-dark: #141414;
    --card-mid: #2a2a2a;
    --card-low: #1c1c1c;
    --band-red: #8e1418;
    --band-cream: #d9cdb4;
    --text-light: #e8e8e8;
    --text-soft: #b9b9b9;
    --text-muted: #8c8c8c;
    --back-ink: #2c2c2c;
    --back-tag: #4a4a4a;
  }
  * { box-sizing: border-box; margin: 0; padding: 0; }
  html, body { width: 1200px; height: 900px; overflow: hidden; }
  body {
    background: radial-gradient(ellipse at 50% 40%, #4a4a4a 0%, var(--stage) 55%, #232323 100%);
    font-family: "Questrial", "Century Gothic", sans-serif;
    position: relative;
  }
  .card {
    position: absolute;
    width: 560px;
    height: 320px;
    border-radius: 18px;
    overflow: hidden;
    box-shadow: 0 18px 40px rgba(0,0,0,.55);
  }

  /* Back side */
  .card-back {
    left: 60px; top: 90px;
    background: linear-gradient(160deg, #1b1b1b 0%, var(--card-dark) 60%, #0e0e0e 100%);
  }
  .card-back .brand-mark {
    position: absolute; left: 0; right: 0; top: 105px;
    text-align: center;
    font-size: 34px; letter-spacing: 3px;
    color: var(--back-ink);
  }
  .card-back .brand-mark .dot {
    display: inline-block; width: 18px; height: 18px; border-radius: 50%;
    background: var(--back-ink); margin-right: 12px; vertical-align: 3px;
  }
  .card-back .tagline {
    position: absolute; left: 0; right: 0; bottom: 60px;
    text-align: center;
    font-family: "Lora", Georgia, serif; font-style: italic;
    font-size: 19px; color: var(--back-tag);
  }

  /* Front side */
  .card-front {
    left: 580px; top: 490px;
    background: linear-gradient(180deg, var(--card-mid) 0%, var(--card-low) 100%);
  }
  .card-front .wave { position: absolute; inset: 0; }
  .card-front .tagline {
    position: absolute; left: 24px; top: 64px;
    font-family: "Lora", Georgia, serif; font-style: italic; font-weight: 600;
    font-size: 16px; color: var(--text-light);
    transform: rotate(-7deg); transform-origin: left bottom;
  }
  .card-front .website {
    position: absolute; left: 110px; top: 80px;
    font-family: "Lora", Georgia, serif; font-style: italic;
    font-size: 14px; color: var(--text-muted);
    transform: rotate(-7deg); transform-origin: left bottom;
  }
  .card-front .brand-name {
    position: absolute; right: 22px; top: 30px;
    font-size: 14px; letter-spacing: 1px; color: var(--band-cream);
    display: flex; align-items: center; gap: 7px;
  }
  .card-front .brand-name .dot {
    width: 12px; height: 12px; border-radius: 50%; background: var(--band-red);
  }
  .person { position: absolute; left: 40px; top: 150px; }
  .person .name { font-size: 23px; color: var(--text-light); }
  .person .role { font-size: 14px; color: var(--text-muted); margin-top: 2px; }
  .contact {
    position: absolute;
    font-size: 15px; color: var(--text-soft);
    display: flex; align-items: center; gap: 10px;
    white-space: nowrap;
  }
  .contact svg { width: 14px; height: 14px; fill: var(--text-soft); flex: none; }
  .mobile { left: 110px; top: 212px; }
  .email  { left: 110px; top: 238px; }
  .address { left: 190px; top: 280px; }
  .office { left: 380px; top: 130px; }
</style>
</head>
<body>

  <section class="card card-back" aria-label="Card back">
    <div class="brand-mark"><span class="dot"></span>NORTHVALE BEER</div>
    <p class="tagline">Premier Craft &amp; Import Beer Distributor</p>
  </section>

  <section class="card card-front" aria-label="Card front">
    <svg class="wave" viewBox="0 0 560 320" preserveAspectRatio="none" aria-hidden="true">
      <defs>
        <linearGradient id="topPanel" x1="0" y1="0" x2="0" y2="1">
          <stop offset="0" stop-color="#1e1e1e"/>
          <stop offset="1" stop-color="#101010"/>
        </linearGradient>
      </defs>
      <path d="M0 0 H560 V72 Q300 78 0 132 Z" fill="url(#topPanel)"/>
      <path d="M0 132 Q300 78 560 72 V80 Q300 86 0 140 Z" fill="var(--band-red)"/>
      <path d="M0 140 Q300 86 560 80 V85 Q300 92 0 146 Z" fill="var(--band-cream)"/>
      <path d="M0 146 Q300 92 560 85 V89 Q300 96 0 150 Z" fill="var(--band-red)"/>
    </svg>

    <p class="tagline">Premier Craft &amp; Import Beer Distributor</p>
    <p class="website">www.northvalebeer.com</p>
    <div class="brand-name"><span class="dot"></span>NORTHVALE BEER</div>

    <div class="person">
      <p class="name">Evan Calder</p>
      <p class="role">Strategy &amp; Acquisitions</p>
    </div>

    <p class="contact mobile">
      <svg viewBox="0 0 14 14"><path d="M4 0h6a1 1 0 0 1 1 1v12a1 1 0 0 1-1 1H4a1 1 0 0 1-1-1V1a1 1 0 0 1 1-1zm0.6 1.5v9.5h4.8V1.5z"/></svg>
      (555) 014-2271
    </p>
    <p class="contact email">
      <svg viewBox="0 0 14 14"><path d="M7 0a7 7 0 1 0 3.5 13.1l-.6-1.1A5.7 5.7 0 1 1 12.7 7c0 1.4-.6 2.1-1.3 2.1s-.9-.5-.9-1.2V3.6H9.3v.6A3.2 3.2 0 1 0 9.6 9.3 2.2 2.2 0 0 0 11.4 10.4C13 10.4 14 9 14 7A7 7 0 0 0 7 0zm0 9a2 2 0 1 1 0-4 2 2 0 0 1 0 4z"/></svg>
      ecalder@mailbox.com
    </p>
    <p class="contact address">
      <svg viewBox="0 0 14 14"><path d="M7 0.5 0 7h2v6.5h3.8V9.5h2.4v4H12V7h2z"/></svg>
      42 Mill Street Riverton, NY 10990
    </p>
    <p class="contact office">
      <svg viewBox="0 0 14 14"><path d="M7 0a7 7 0 1 0 0 14A7 7 0 0 0 7 0zm0 1.4a5.6 5.6 0 1 1 0 11.2A5.6 5.6 0 0 1 7 1.4zM5 3.5 4 4.5c0 3 2.5 5.5 5.5 5.5l1-1-1.6-1.5-.9.7A4 4 0 0 1 6 6.2l.7-.9z"/></svg>
      (555) 019-3300
    </p>
  </section>

</body>
</html>
```